Geschäftspapiere für Unternehmensberatung
Zielgruppe
Wir machen Unternehmensberatung, Prozessoptimierung, Change Management,
Buchhaltung.
Unsere Zielgruppe sind Firmen, denen es wirtschaftlich nicht so gut geht und die Hilfe benötigen.
Aufgabenstellung
Wir möchten ein CI an unser Logo angepasst.
Es darf gerne etwas besonderes sein.

```html
<!DOCTYPE html>
<html lang="de">
<head>
<meta charset="utf-8">
<title>Korvan Beratung – Briefbogen</title>
<link href="https://fonts.googleapis.com/css2?family=Montserrat:wght@400;500&display=swap" rel="stylesheet">
<style>
  :root {
    --backdrop: #d6d6d6;
    --paper: #ffffff;
    --ink-grey: #7d7b7b;
    --ink-soft: #8a8888;
    --brand-blue: #2a5d9b;
    --band-grey: #8a8686;
    --rule: #c9c9c9;
    --watermark: #eef0f3;
  }
  * { margin: 0; padding: 0; box-sizing: border-box; }
  html, body {
    width: 1200px; height: 900px; overflow: hidden;
    background: var(--backdrop);
    font-family: "Montserrat", sans-serif;
  }
  .letterhead {
    position: absolute;
    left: 302px; top: 30px;
    width: 595px; height: 840px;
    background: var(--paper);
    box-shadow: 0 2px 10px rgba(0,0,0,0.12);
    overflow: hidden;
  }
  .brand {
    position: absolute; right: 48px; top: 50px;
    display: flex; align-items: center; gap: 8px;
  }
  .brand-dot {
    width: 14px; height: 14px; border-radius: 50%;
    background: var(--brand-blue);
  }
  .brand-name {
    font-size: 17px; font-weight: 500; letter-spacing: 1.5px;
    color: var(--brand-blue); text-transform: uppercase;
  }
  .watermark {
    position: absolute; left: 178px; top: 352px;
    width: 228px; height: 228px; border-radius: 50%;
    border: 14px solid var(--watermark);
  }
  .sender {
    position: absolute; left: 435px; top: 117px;
    color: var(--ink-grey);
  }
  .sender-name { font-size: 11.5px; font-weight: 500; margin-bottom: 6px; }
  .sender-list { list-style: none; font-size: 9.5px; line-height: 12.3px; }
  .sender-list li { display: flex; align-items: flex-start; gap: 7px; }
  .sender-list svg { width: 9px; height: 9px; margin-top: 1.5px; flex: none; }
  .footer-rule {
    position: absolute; left: 26px; top: 730px;
    width: 274px; height: 1px; background: var(--rule);
  }
  .legal {
    position: absolute; left: 33px; top: 746px;
    font-size: 9.5px; line-height: 12px; color: var(--ink-soft);
  }
  .legal-manager { margin-bottom: 7px; }
  .legal-columns { display: flex; gap: 16px; }
  .legal-columns p { width: 140px; }
  .band-grey {
    position: absolute; left: 0; top: 826px;
    width: 422px; height: 14px; background: var(--band-grey);
  }
  .band-blue {
    position: absolute; left: 427px; top: 826px;
    width: 168px; height: 14px; background: var(--brand-blue);
  }
</style>
</head>
<body>
  <main class="letterhead">
    <div class="brand">
      <span class="brand-dot"></span>
      <span class="brand-name">Korvan Beratung</span>
    </div>

    <div class="watermark" aria-hidden="true"></div>

    <address class="sender" style="font-style:normal">
      <p class="sender-name">korvan-beratung UG</p>
      <ul class="sender-list">
        <li>
          <svg viewBox="0 0 10 10" fill="none" stroke="var(--brand-blue)" stroke-width="1.2"><path d="M5 8.2C3 6 2 4.8 2 3.6a3 3 0 0 1 6 0C8 4.8 7 6 5 8.2z"/><circle cx="5" cy="3.6" r="1"/><path d="M3 9.6h4"/></svg>
          <span>Lindenweg 48<br>31582 Nordhavel</span>
        </li>
        <li>
          <svg viewBox="0 0 10 10" fill="none" stroke="var(--brand-blue)" stroke-width="1.2"><path d="M2 1.2l1.8 1.8-1 1.2a6 6 0 0 0 3 3l1.2-1 1.8 1.8-1.2 1.2C4.6 9 1 5.4.8 2.4z"/></svg>
          <span>0172/ 4410857</span>
        </li>
        <li>
          <svg viewBox="0 0 10 10" fill="none" stroke="var(--brand-blue)" stroke-width="1.2"><rect x="0.8" y="2" width="8.4" height="6.2"/><path d="M1 2.4l4 3 4-3"/></svg>
          <span>marquart@korvan-b.de</span>
        </li>
      </ul>
    </address>

    <div class="footer-rule"></div>
    <footer class="legal">
      <p class="legal-manager">Geschäftsführerin: Helena Marquart</p>
      <div class="legal-columns">
        <p>Kreissparkasse Nordhavel<br>DE41 2716 0500 0071 5528 14<br>KSNHDE21XXX</p>
        <p>Amtsgericht Nordhavel<br>HRB518207<br>USt-IdNr: DE416203775</p>
      </div>
    </footer>

    <div class="band-grey"></div>
    <div class="band-blue"></div>
  </main>
</body>
</html>
```